label for health supplement

The supplement targets cardiovascular diseases.
The size is: 146 mm and height 54 mm
The name of the product is: Velmora Pulse
I will need the source file as we'll probably be required to make modifications to be fully NRB compliant.
It should contain the following text lines on it:

VELMORA PULSE
HEALTH FOOD GMP & ISO9001 COMPLIANT
DIETARY SUPPLEMENT
60 CAPSULES

Foundation for Longer Life
Essential For Cardiovascular Health
Scientifically-designed supplement
Lowers cholesterol level

Suggested Use
Take one or two capsules daily, or as directed by a physician.

Not intended for children or pregnant women.
Consult a healthcare practitioner prior to use.
Store in a cool dry place away from children
These statements have not been evaluated by the National Remedy Bureau. This product is not intended to diagnose, treat, cure or prevent any disease.

The part below should look like:

http://7.cdn.quorvanta.example/-9k2hTzWqRmD/XPLTa8MnBeE/BBBBBBBBBkQ/HwepLo5RGyc/s1600/8-oz-nutritional-panel.jpg

Supplement Facts
Serving Size: 2 Softgels
Servings per Container: 45
Amount Per Serving % Daily Value
Calories 5
Calories from Fat 5 3%*
Total Fat 0.5 g
Saturated Fat 0 g 0%*
Vitamin E (as d-alpha tocopherol) 1 IU 3%
Vitamin A 90-95 IU 90 4%-8%
Vitamin D 0-5 IU 0 (5) 0% - 1%
Omega-3 Fatty Acids 140 mg *
EPA (Eicosapentaenoic Acid) 45 mg *
DHA (Docosahexaenoic Acid) 70 mg *
Other Omega-3s 25 mg *
*Daily value not established.

Target Market(s)

The target market is made by people from 35-80 years old since they are the most suffering from cardiovascular diseases.

Industry/Entity Type

Healthcare

Colors

Designer to choose colors to be used in the design.

Requirements
Must have
• I must receive the source file since I will probably need to make more modifications in the future to it based on registration requirements.

```html
<!DOCTYPE html>
<html lang="en">
<head>
<meta charset="utf-8">
<title>Velmora Pulse – Supplement Label</title>
<link href="https://fonts.googleapis.com/css2?family=Arimo:wght@400;700&display=swap" rel="stylesheet">
<style>
  :root {
    --brand-red: #d7141a;
    --ink: #1a1a1a;
    --ring-grey: #b9b9b9;
    --paper: #ffffff;
    --muted: #444444;
  }
  * { box-sizing: border-box; margin: 0; padding: 0; }
  html, body { width: 1200px; height: 443px; overflow: hidden; background: var(--paper); }
  body { font-family: "Arimo", Arial, sans-serif; color: var(--ink); }
  .label { position: relative; width: 1200px; height: 443px; background: var(--paper); }

  /* Brand seal */
  .seal {
    position: absolute; left: 8px; top: 18px; width: 262px; height: 262px;
    border-radius: 50%; border: 16px solid var(--ring-grey);
    display: flex; flex-direction: column; align-items: center; justify-content: center;
    text-align: center;
  }
  .seal__name { color: var(--brand-red); font-weight: 700; font-size: 27px; line-height: 1.02; letter-spacing: -0.5px; }
  .seal__cert { color: var(--brand-red); font-size: 10.5px; font-weight: 700; margin-top: 10px; }
  .seal__type { font-size: 14px; margin-top: 8px; color: var(--muted); }
  .seal__count { color: var(--brand-red); font-weight: 700; font-size: 17px; margin-top: 4px; }

  /* Benefits */
  .benefits { position: absolute; left: 335px; top: 20px; list-style: none; }
  .benefits li { display: flex; align-items: center; font-size: 17px; height: 28px; }
  .benefits .dot { width: 15px; height: 15px; border-radius: 50%; background: var(--brand-red); margin-right: 12px; flex: none; }

  .usage { position: absolute; left: 335px; top: 143px; width: 470px; }
  .usage h2 { font-size: 15px; font-weight: 700; color: var(--ink); }
  .usage p { font-size: 12.5px; margin-top: 3px; }

  .warning {
    position: absolute; left: 335px; top: 186px; width: 322px; height: 140px;
    border: 2px solid var(--brand-red); padding: 8px 10px;
    font-size: 11.6px; line-height: 1.35; color: var(--ink);
  }

  /* Supplement facts */
  .facts {
    position: absolute; left: 838px; top: 6px; width: 350px; height: 430px;
    border: 2px solid var(--ink); padding: 4px 8px; font-size: 12px;
  }
  .facts h1 { font-size: 27px; font-weight: 700; line-height: 1.05; letter-spacing: -0.5px; }
  .facts .serving { font-size: 12px; line-height: 1.35; }
  .facts .bar-thick { height: 9px; background: var(--ink); margin: 3px 0; }
  .facts .bar-mid { height: 4px; background: var(--ink); margin: 2px 0; }
  .row { display: flex; justify-content: space-between; border-bottom: 1px solid var(--ink); padding: 3px 0; line-height: 1.2; }
  .row--head { font-weight: 700; }
  .row--indent .row__name { padding-left: 14px; }
  .row__name b { font-weight: 700; }
  .row__dv { min-width: 58px; text-align: left; }
  .facts .note { font-size: 11px; margin-top: 6px; }
</style>
</head>
<body>
<main class="label">
  <section class="seal">
    <div class="seal__name">VELMORA<br>PULSE</div>
    <div class="seal__cert">HEALTH FOOD GMP &amp; ISO9001 COMPLIANT</div>
    <div class="seal__type">DIETARY SUPPLEMENT</div>
    <div class="seal__count">60 CAPSULES</div>
  </section>

  <ul class="benefits">
    <li><span class="dot"></span>Foundation for Longer Life</li>
    <li><span class="dot"></span>Essential For Cardiovascular Health</li>
    <li><span class="dot"></span>Scientifically-designed supplement</li>
    <li><span class="dot"></span>Lowers cholesterol level</li>
  </ul>

  <section class="usage">
    <h2>Suggested Use</h2>
    <p>Take one or two capsules daily, or as directed by a physician.</p>
  </section>

  <section class="warning">
    Not intended for children or pregnant women.
    Consult a healthcare practitioner prior to use.
    Store in a cool dry place away from children
    These statements have not been evaluated by the National Remedy Bureau. This product is not intended to diagnose, treat, cure or prevent any disease.
  </section>

  <section class="facts">
    <h1>Supplement Facts</h1>
    <div class="serving">Serving Size: 2 Softgels<br>Servings per Container: 45</div>
    <div class="bar-thick"></div>
    <div class="row row--head"><span>Amount Per Serving</span><span>% Daily Value</span></div>
    <div class="row"><span class="row__name"><b>Calories</b> 5</span><span class="row__dv"></span></div>
    <div class="row row--indent"><span class="row__name">Calories from Fat 5</span><span class="row__dv">3%*</span></div>
    <div class="row"><span class="row__name"><b>Total Fat</b> 0.5 g</span><span class="row__dv"></span></div>
    <div class="row row--indent"><span class="row__name">Saturated Fat 0 g</span><span class="row__dv">0%*</span></div>
    <div class="row"><span class="row__name">Vitamin E (as d-alpha tocopherol) 1 IU</span><span class="row__dv">3%</span></div>
    <div class="row"><span class="row__name">Vitamin A 90-95 IU 90</span><span class="row__dv">4%-8%</span></div>
    <div class="row"><span class="row__name">Vitamin D 0-5 IU 0 (5)</span><span class="row__dv">0% - 1%</span></div>
    <div class="row"><span class="row__name"><b>Omega-3 Fatty Acids</b> 140 mg</span><span class="row__dv">*</span></div>
    <div class="row row--indent"><span class="row__name">EPA (Eicosapentaenoic Acid) 45 mg</span><span class="row__dv">*</span></div>
    <div class="row row--indent"><span class="row__name">DHA (Docosahexaenoic Acid) 70 mg</span><span class="row__dv">*</span></div>
    <div class="row row--indent"><span class="row__name">Other Omega-3s 25 mg</span><span class="row__dv">*</span></div>
    <div class="bar-mid"></div>
    <p class="note">*Daily value not established.</p>
  </section>
</main>
</body>
</html>
```